Wordpress Design for my Consulting Company

We want a WordPress site created for our new business. We have created a mock-up of the content we want on the site at https://marcobellweather.example.com/website-5

We are not attached to any of the pictures and just put stock stuff from bloq's editor, which we don't have rights to use outside of bloq.

We are NOT looking to just port this site to WordPress, we are looking for some creative ways to display the content in a more professional artistic sense.

I have included several logo files and a text file with the colors and Fonts used in the logo. We are not looking to change the logo or the colors used in the logo.

The Schedule appointment links to a page that embeds a bookslot.example calendar. https://bookslot.example.com/marco-bellweather/trailguide

The final website domain will be venturelanterns.example

Venture lanterns is a consulting company that works directly with the business owners and leaders of small businesses between 50-200 employees. We help companies make sure they have the right technology to meet their strategic goals. We are the anti-"Computer Guy" and we focus on business outcomes NOT cool technology gadgets.

The final design should communicate business growth and success.

Target Market(s)

Business Owners of companies with 50-200 employees

Coding

Coded - Design and coding required

Number of Pages Required

1 page

Font styles to use
Serif
Other font styles liked:
• Trajan Pro Bold, Open Sans

Requirements
Must have
• Should focus on consulting rather than technology.
• Should show the customer as the hero and we are just their guide.
• Must use the logo provided and the colors and fonts in the text file provided. Any other colors and fonts must be complementary.
• The design should scale for all devices computer, iPad, or phone
Should not have
• Should not focus on technology, we are the anti-"Computer Guy" and we focus on business outcomes NOT cool technology gadgets.

```html
<!DOCTYPE html>
<html lang="en">
<head>
<meta charset="utf-8">
<title>Venture Lanterns — Technology Advisors That Get Business</title>
<link rel="stylesheet" href="https://fonts.googleapis.com/css2?family=Cinzel:wght@400;700&family=Open+Sans:wght@400;600;700&family=Caveat:wght@500&display=swap">
<style>
:root{
  --orange:#c8773f;
  --orange-dark:#b5652f;
  --slate:#3d4a54;
  --slate-deep:#2f3a43;
  --ink:#2c3640;
  --text:#5b6167;
  --muted:#8a9096;
  --paper:#ffffff;
  --mist:#f3f4f4;
  --cell-a:#eeeff0;
  --cell-b:#f5f2ed;
}
*{box-sizing:border-box;margin:0;padding:0}
html,body{width:1200px;height:2624px;overflow:hidden;background:var(--paper)}
body{font-family:"Open Sans",Arial,sans-serif;color:var(--text);position:relative}
.section{position:absolute;left:0;width:1200px;overflow:hidden}
.accent{color:var(--orange)}

/* header */
.site-header{top:0;height:88px;background:var(--paper)}
.brand{position:absolute;left:255px;top:22px;display:flex;align-items:center;gap:10px}
.brand-dot{width:44px;height:44px;border-radius:50%;background:var(--slate)}
.brand-name{font-family:"Cinzel",Georgia,serif;font-weight:700;font-size:17px;color:var(--ink);line-height:1}
.main-nav{position:absolute;right:255px;top:40px;display:flex;gap:22px;font-size:9px;letter-spacing:.6px;color:var(--ink);text-transform:uppercase}

/* hero */
.hero{top:88px;height:414px;background:linear-gradient(180deg,#5a6877 0%,#4a5663 55%,#6e6a66 100%);overflow:visible;z-index:2}
.hero-photo{position:absolute;inset:0;background:radial-gradient(ellipse at 20% 40%,rgba(40,52,66,.6),transparent 60%),linear-gradient(90deg,rgba(46,58,72,.4),rgba(180,120,80,.25))}
.hero-inner{position:absolute;left:0;right:0;top:100px;text-align:center;color:#fff}
.hero-kicker{font-size:11px;letter-spacing:2.4px;font-weight:600;text-transform:uppercase}
.hero-rule{width:30px;height:2px;background:var(--orange);margin:12px auto 14px}
.hero-title{font-family:"Cinzel",Georgia,serif;font-weight:700;font-size:35px;line-height:40px;letter-spacing:.5px}
.hero-actions{display:flex;justify-content:center;gap:12px;margin-top:24px}
.btn{display:inline-flex;align-items:center;gap:10px;height:34px;padding:0 18px;font-size:10px;letter-spacing:1px;text-transform:uppercase;color:#fff;font-weight:600}
.btn-primary{background:var(--orange)}
.btn-dark{background:var(--slate)}
.hero-notch{position:absolute;left:580px;bottom:-9px;width:40px;height:10px}

/* why */
.why{top:502px;height:438px;background:var(--paper)}
.section-title{font-family:"Cinzel",Georgia,serif;font-weight:700;font-size:21px;color:var(--ink);text-align:center;letter-spacing:.5px}
.section-sub{font-size:12px;color:var(--ink);text-align:center}
.why .section-title{position:absolute;top:46px;left:0;right:0}
.why .section-sub{position:absolute;top:88px;left:0;right:0}
.gripe{position:absolute;width:215px;font-family:"Caveat",cursive;font-size:15px;line-height:16px;color:var(--orange);padding-bottom:10px;border-bottom:1px solid #e6e6e6}
.gripe.left{left:245px;text-align:right;padding-right:22px}
.gripe.right{left:742px;text-align:left;padding-left:22px}
.gripe .tick{position:absolute;top:2px;width:11px;height:11px}
.gripe.left .tick{right:0}
.gripe.right .tick{left:0}
.why-photo{position:absolute;left:467px;top:128px;width:266px;height:266px;border-radius:50%;border:4px solid var(--slate);border-left-color:var(--orange);border-bottom-color:var(--orange);padding:6px}
.why-photo span{display:block;width:100%;height:100%;border-radius:50%;background:radial-gradient(circle at 50% 45%,#d8d9da,#9ea3a7 70%,#6f757b)}

/* what */
.what{top:935px;height:430px;background:linear-gradient(110deg,#a2704d 0%,#5b5553 35%,var(--slate) 60%,var(--slate) 100%)}
.what-edge{position:absolute;left:0;top:0;width:1200px;height:30px}
.what-photo{position:absolute;left:243px;top:90px;width:340px;height:215px;background:linear-gradient(135deg,#a9b0b0 0%,#8c9495 50%,#6c7373 100%);box-shadow:0 4px 14px rgba(0,0,0,.3)}
.what-caption{position:absolute;left:243px;width:340px;text-align:center;top:318px}
.what-caption .lead{font-family:"Cinzel",Georgia,serif;font-weight:700;font-size:11px;color:#fff}
.what-caption .point{font-family:"Cinzel",Georgia,serif;font-size:14px;color:var(--orange);margin-top:4px}
.what-copy{position:absolute;left:615px;top:115px;width:330px;text-align:center;color:#e6e9eb;font-size:10.5px;line-height:16px}
.what-copy .section-title{color:#fff;margin-bottom:18px}
.what-copy p{margin-bottom:12px}
.what-copy .btn{margin-top:6px}

/* how */
.how{top:1365px;height:473px;background:var(--paper)}
.how .section-title{position:absolute;top:52px;left:0;right:0}
.how .section-sub{position:absolute;top:96px;left:0;right:0}
.steps{position:absolute;left:243px;top:150px;width:714px;height:247px;display:flex}
.step{flex:1;position:relative;text-align:center;padding-top:26px}
.step:nth-child(odd){background:var(--cell-a)}
.step:nth-child(even){background:var(--cell-b)}
.step-icon{width:40px;height:40px;margin:0 auto}
.step-name{font-family:"Caveat",cursive;font-size:17px;color:var(--ink);letter-spacing:1px;margin-top:12px}
.step-rule{width:14px;height:2px;background:var(--orange);margin:6px auto 12px}
.step-text{font-size:9.5px;line-height:14px;padding:0 18px;color:var(--text)}
.step-num{position:absolute;left:0;right:0;bottom:14px;font-size:38px;font-weight:700;color:rgba(0,0,0,.05)}

/* testimonials */
.testimonials{top:1838px;height:357px;background:linear-gradient(100deg,#4a5a66 0%,#56626a 45%,#8d6f58 75%,#c17b45 100%)}
.testimonials .section-title{position:absolute;top:46px;left:0;right:0;color:#fff}
.quote-mark{position:absolute;left:586px;top:85px;width:28px;height:26px}
.quote-text{position:absolute;left:370px;width:460px;top:138px;text-align:center;font-style:italic;color:#fff;font-size:10.5px;line-height:19px}
.avatar{position:absolute;left:583px;top:214px;width:34px;height:34px;border-radius:50%;background:#b88e6a;border:2px solid #fff}
.client-name{position:absolute;left:0;right:0;top:260px;text-align:center;font-size:11px;font-weight:700;color:var(--orange)}
.client-role{position:absolute;left:0;right:0;top:276px;text-align:center;font-size:9px;color:#fff}
.slider-dot{position:absolute;left:597px;top:300px;width:5px;height:5px;border-radius:50%;background:#fff}
.arrow{position:absolute;top:205px;width:10px;height:14px}

/* contact */
.contact{top:2195px;height:335px;background:var(--mist)}
.contact .section-title{position:absolute;left:350px;top:34px}
.info{position:absolute;left:270px;font-size:9.5px;color:var(--text)}
.info h4{font-family:"Cinzel",Georgia,serif;font-size:11px;color:var(--ink);display:flex;align-items:center;gap:8px;margin-bottom:8px;letter-spacing:.5px}
.info h4 svg{width:13px;height:13px}
.info p{line-height:14px}
.message-panel{position:absolute;left:597px;top:0;width:353px;height:335px;background:var(--slate)}
.message-panel h3{position:absolute;left:30px;top:34px;font-family:"Cinzel",Georgia,serif;font-weight:700;color:#fff;font-size:11px;letter-spacing:1.2px}
.field{position:absolute;left:30px;width:290px;background:#fff;font-size:7.5px;color:#a3a8ad;letter-spacing:.8px;padding:7px 8px}
.submit{position:absolute;left:30px;top:234px;width:112px;height:28px;background:var(--orange);color:#fff;font-size:9px;letter-spacing:1px;font-weight:600;display:flex;align-items:center;justify-content:center}
.contact-band{position:absolute;left:0;bottom:0;width:1200px;height:26px}

/* footer */
.site-footer{top:2530px;height:94px;background:#eeeeee}
.site-footer .brand{top:24px}
.social{position:absolute;right:255px;top:22px;display:flex;gap:8px}
.social span{width:20px;height:20px;border-radius:50%;border:1px solid #9aa0a5}
.copyright{position:absolute;right:255px;top:58px;font-size:8.5px;color:var(--muted)}
</style>
</head>
<body>

<header class="section site-header">
  <div class="brand"><span class="brand-dot"></span><span class="brand-name">Venture Lanterns</span></div>
  <nav class="main-nav"><span>Why us</span><span>What we do</span><span>How we do it</span><span>Testimonials</span><span>Contact</span></nav>
</header>

<section class="section hero">
  <div class="hero-photo" role="img" aria-label="Businessman opening his shirt like a hero in front of a city skyline at dusk"></div>
  <div class="hero-inner">
    <p class="hero-kicker">Technology advisors that <span class="accent">get</span> business</p>
    <div class="hero-rule"></div>
    <h1 class="hero-title">We help you leverage<br>technology to create a<br>competitive advantage.</h1>
    <div class="hero-actions">
      <span class="btn btn-primary">Schedule appointment <svg width="10" height="6" viewBox="0 0 10 6"><path d="M0 3h8M6 0.5 9 3 6 5.5" stroke="#fff" fill="none" stroke-width="1.3"/></svg></span>
      <span class="btn btn-dark">Keep learning more <svg width="10" height="6" viewBox="0 0 10 6"><path d="M0 3h8M6 0.5 9 3 6 5.5" stroke="#fff" fill="none" stroke-width="1.3"/></svg></span>
    </div>
  </div>
  <svg class="hero-notch" viewBox="0 0 40 10"><path d="M0 0 Q20 14 40 0Z" fill="#6e6a66"/></svg>
</section>

<section class="section why">
  <h2 class="section-title"><span class="accent">Why</span> Venture Lanterns ?</h2>
  <p class="section-sub">Are you tired of "Computer Guys" that...</p>

  <div class="gripe left" style="top:158px">Don't want to be involved in business strategy.<svg class="tick" viewBox="0 0 12 12"><circle cx="6" cy="6" r="6" fill="#3d4a54"/><path d="M3 6.2 5.2 8.3 9 4" stroke="#fff" stroke-width="1.5" fill="none"/></svg></div>
  <div class="gripe left" style="top:230px">Say "No" but do not give options on how to achieve your business outcome.<svg class="tick" viewBox="0 0 12 12"><circle cx="6" cy="6" r="6" fill="#3d4a54"/><path d="M3 6.2 5.2 8.3 9 4" stroke="#fff" stroke-width="1.5" fill="none"/></svg></div>
  <div class="gripe left" style="top:308px;border-bottom:none">Can't explain how a technology will create business value, but insist it is necessary.<svg class="tick" viewBox="0 0 12 12"><circle cx="6" cy="6" r="6" fill="#3d4a54"/><path d="M3 6.2 5.2 8.3 9 4" stroke="#fff" stroke-width="1.5" fill="none"/></svg></div>

  <div class="why-photo"><span role="img" aria-label="Frustrated man resting his head on a laptop keyboard"></span></div>

  <div class="gripe right" style="top:158px">Give you the excuse, "You never asked."<svg class="tick" viewBox="0 0 12 12"><circle cx="6" cy="6" r="6" fill="#3d4a54"/><path d="M3 6.2 5.2 8.3 9 4" stroke="#fff" stroke-width="1.5" fill="none"/></svg></div>
  <div class="gripe right" style="top:220px">Recommend technology when a simple process or policy change would have the same effect.<svg class="tick" viewBox="0 0 12 12"><circle cx="6" cy="6" r="6" fill="#3d4a54"/><path d="M3 6.2 5.2 8.3 9 4" stroke="#fff" stroke-width="1.5" fill="none"/></svg></div>
  <div class="gripe right" style="top:308px">Suggest expensive solutions that are just thrown away, soon after they are deployed.<svg class="tick" viewBox="0 0 12 12"><circle cx="6" cy="6" r="6" fill="#3d4a54"/><path d="M3 6.2 5.2 8.3 9 4" stroke="#fff" stroke-width="1.5" fill="none"/></svg></div>
</section>

<section class="section what">
  <svg class="what-edge" viewBox="0 0 1200 30" preserveAspectRatio="none"><path d="M0 0H1200V0L0 18Z" fill="#fff"/><path d="M0 18 1200 0V6L0 24Z" fill="#b9bcbf"/></svg>
  <div class="what-photo" role="img" aria-label="Businessman with a briefcase standing at a fork in a path facing a city skyline"></div>
  <div class="what-caption"><p class="lead">We Get...</p><p class="point">Eliminating bottlenecks</p></div>
  <div class="what-copy">
    <h2 class="section-title"><span class="accent">What</span> we do</h2>
    <p>We get the frustration of working with consultants and experts who don't listen or take the time to understand your company goals and vision. We believe technology should serve your business, not the other way around.</p>
    <p>Computer guys frustrate business leaders because they don't have a business mindset. Venture Lanterns advises on strategy that helps companies apply technology to gain a competitive advantage.</p>
    <span class="btn btn-primary">Schedule appointment <svg width="10" height="6" viewBox="0 0 10 6"><path d="M0 3h8M6 0.5 9 3 6 5.5" stroke="#fff" fill="none" stroke-width="1.3"/></svg></span>
  </div>
</section>

<section class="section how">
  <h2 class="section-title"><span class="accent">How</span> we do it</h2>
  <p class="section-sub">The Four Steps to Aligning Technology to your Business Strategy!</p>
  <div class="steps">
    <div class="step">
      <svg class="step-icon" viewBox="0 0 40 40"><circle cx="20" cy="17" r="9" fill="none" stroke="#3d4a54" stroke-width="1.6"/><path d="M16 27h8M17 31h6" stroke="#c8773f" stroke-width="1.6"/></svg>
      <p class="step-name">01.DISCOVER</p><div class="step-rule"></div>
      <p class="step-text">Identify what is going on behind the scenes, and create a snapshot of the current infrastructure.</p>
      <span class="step-num">01</span>
    </div>
    <div class="step">
      <svg class="step-icon" viewBox="0 0 40 40"><rect x="6" y="6" width="12" height="10" fill="none" stroke="#c8773f" stroke-width="1.6"/><rect x="20" y="18" width="14" height="14" fill="none" stroke="#3d4a54" stroke-width="1.6"/><path d="M12 16v9h8" stroke="#3d4a54" stroke-width="1.6" fill="none"/></svg>
      <p class="step-name">02.PRIORITIZE</p><div class="step-rule"></div>
      <p class="step-text">Meet to decide which solutions and policies will have the greatest impact on reaching the companies goals.</p>
      <span class="step-num">02</span>
    </div>
    <div class="step">
      <svg class="step-icon" viewBox="0 0 40 40"><rect x="8" y="6" width="24" height="28" fill="none" stroke="#3d4a54" stroke-width="1.6"/><path d="M13 26l5-6 4 3 6-8" stroke="#c8773f" stroke-width="1.6" fill="none"/></svg>
      <p class="step-name">03.IMPLEMENT</p><div class="step-rule"></div>
      <p class="step-text">Implement those things that will give you the greatest return on investment.</p>
      <span class="step-num">03</span>
    </div>
    <div class="step">
      <svg class="step-icon" viewBox="0 0 40 40"><circle cx="15" cy="16" r="7" fill="none" stroke="#3d4a54" stroke-width="1.6"/><circle cx="15" cy="16" r="2.5" fill="#c8773f"/><circle cx="27" cy="27" r="5" fill="none" stroke="#3d4a54" stroke-width="1.6"/><circle cx="27" cy="27" r="1.8" fill="#c8773f"/></svg>
      <p class="step-name">04.MAINTAIN</p><div class="step-rule"></div>
      <p class="step-text">Create a system that keeps your technology aligned as strategy adjusts over time.</p>
      <span class="step-num">04</span>
    </div>
  </div>
</section>

<section class="section testimonials" role="img" aria-label="Businessman with a briefcase walking along an open road into the distance">
  <h2 class="section-title"><span class="accent">Client</span> testimonials</h2>
  <svg class="quote-mark" viewBox="0 0 28 26"><path d="M2 26V14Q2 3 12 1V6Q7 8 7 13H12V26ZM16 26V14Q16 3 26 1V6Q21 8 21 13H26V26Z" fill="#c8773f"/></svg>
  <p class="quote-text">I knew I was behind, I just didn't know by how much. We had years of band-aided solutions and Venture Lanterns helped us stabilize our environment and position ourselves to compete in the quickly changing world of copy and print.</p>
  <svg class="arrow" style="left:253px" viewBox="0 0 10 14"><path d="M8 1 2 7l6 6" stroke="#fff" stroke-width="2" fill="none"/></svg>
  <svg class="arrow" style="left:937px" viewBox="0 0 10 14"><path d="M2 1l6 6-6 6" stroke="#fff" stroke-width="2" fill="none"/></svg>
  <span class="avatar"></span>
  <p class="client-name">Dale Renner</p>
  <p class="client-role">Founder, Print Harbor</p>
  <span class="slider-dot"></span>
</section>

<section class="section contact">
  <h2 class="section-title"><span class="accent">Contact</span> us</h2>
  <div class="info" style="top:82px">
    <h4><svg viewBox="0 0 14 14"><circle cx="7" cy="7" r="7" fill="#c8773f"/><path d="M7 3a2.5 2.5 0 0 1 2.5 2.5C9.5 7.5 7 11 7 11S4.5 7.5 4.5 5.5A2.5 2.5 0 0 1 7 3Z" fill="#fff"/></svg>Our Address</h4>
    <p>1450 Meridian Parkway South, Suite 200,<br>Brookfield, TX 77001</p>
  </div>
  <div class="info" style="top:146px">
    <h4><svg viewBox="0 0 14 14"><circle cx="7" cy="7" r="7" fill="#c8773f"/><path d="M4.5 3.5 6 5 5.2 6.2Q6 8 7.8 8.8L9 8l1.5 1.5L9.5 10.7Q6.5 10.5 3.3 7.2 3 5.5 4.5 3.5Z" fill="#fff"/></svg>Call us</h4>
    <p>(555) 014-0580</p>
  </div>
  <div class="info" style="top:198px">
    <h4><svg viewBox="0 0 14 14"><circle cx="7" cy="7" r="7" fill="#c8773f"/><rect x="3.5" y="4.5" width="7" height="5" fill="#fff"/><path d="M3.5 4.5 7 7.5l3.5-3" stroke="#c8773f" fill="none"/></svg>E-mail</h4>
    <p>mbellweather@venturelanterns.example</p>
  </div>
  <div class="message-panel">
    <h3>Send us a message</h3>
    <div class="field" style="top:62px;height:28px">NAME</div>
    <div class="field" style="top:102px;height:28px">EMAIL</div>
    <div class="field" style="top:142px;height:78px">MESSAGE</div>
    <div class="submit">SUBMIT</div>
  </div>
  <svg class="contact-band" viewBox="0 0 1200 26" preserveAspectRatio="none"><path d="M0 26 1200 4V26Z" fill="#c8773f"/></svg>
</section>

<footer class="section site-footer">
  <div class="brand"><span class="brand-dot"></span><span class="brand-name">Venture Lanterns</span></div>
  <div class="social"><span></span><span></span><span></span></div>
  <p class="copyright">Copyright © 2018 Venture Lanterns. All Rights Reserved.</p>
</footer>

</body>
</html>
```